Site for company producing and selling products for children's health

We need an appealing professional web site design and images for a brand new company producing and selling products focused on children’s health. The site will offer information to visitors on the company, the company’s products, and general resources related to children’s health. Additionally the site will offer e-commerce functionality to allow for ordering of the company’s products.
The content and navigation for the site will be generated by programming, such as php or asp, and therefore any images used in the navigation portions of the site should allow for HTML markup to be overlaid rather than having the text built into the image or graphic.
The design must include 2 layouts, one for the landing/home page that includes only top navigation, and an inner page layout that includes both top and left navigation.
The header area of the site should include a place for links to access the visitor’s cart and profile similar to the top sections of plumvat.com, tidelor.com, and keenmart.com.
The landing page of the site should include some type of “changing” image area where we can include multiple image files for rotation to visitors similar to what is seen at vorta.com or brisksip.com. The flash/animation mechanism does not need to be provided (although it would be a plus if it was) but the design must accommodate the space for it.
The company’s colors are Orange (FF9900) and Blue (0066FF) and the logo can be viewed at http://wonkibrook.com/logo.png
All CSS and markup provided must be display consistently in Internet Explorer 7+, FifeFox, Google Chrome, and Safari.
Incorporating social media links (facebook, twitter, etc.) is desirable.
Parents who are conscious of health risks associated with children's diets and consumer food products.
E-Commerce

```html
<!DOCTYPE html>
<html lang="en">
<head>
<meta charset="utf-8">
<title>wonkibrook – Inner page</title>
<link rel="stylesheet" href="https://fonts.googleapis.com/css2?family=PT+Sans:wght@400;700&display=swap">
<style>
  :root {
    --orange: #ff9900;
    --blue: #0066ff;
    --ink: #111111;
    --text: #2a2a2a;
    --tab: #dedede;
    --card: #f4f4f4;
    --footer: #454545;
    --footer-text: #e6e6e6;
    --header-top: #dcdcdc;
  }
  * { box-sizing: border-box; margin: 0; padding: 0; }
  html, body { width: 1200px; height: 900px; overflow: hidden; }
  body {
    position: relative;
    background: #ffffff;
    font-family: "PT Sans", "Trebuchet MS", sans-serif;
    color: var(--ink);
  }
  .site-header {
    position: absolute; left: 0; top: 0; width: 1200px; height: 112px;
    background: linear-gradient(to bottom, var(--header-top), #ffffff);
  }
  .brand {
    position: absolute; left: 100px; top: 66px;
    display: flex; align-items: center; gap: 8px;
    font-size: 27px; font-weight: 700; color: var(--orange);
    line-height: 1;
  }
  .brand-mark { width: 14px; height: 14px; border-radius: 50%; background: var(--blue); }
  .main-nav {
    position: absolute; left: 295px; top: 67px;
    display: flex; gap: 40px; list-style: none;
  }
  .main-nav a { color: var(--ink); text-decoration: none; font-size: 29px; line-height: 1; }
  .account-bar {
    position: absolute; left: 851px; top: 13px; font-size: 13.5px; color: var(--ink);
  }
  .account-bar a { color: var(--ink); text-decoration: none; margin-left: 8px; }
  .cart { position: absolute; left: 1040px; top: 16px; width: 62px; text-align: center; }
  .cart svg { display: block; margin: 0 0 0 2px; }
  .cart-count { font-size: 13px; margin-top: 2px; }

  .side-nav {
    position: absolute; left: 100px; top: 125px; width: 140px; height: 240px;
    border-radius: 8px 0 0 0;
    background: linear-gradient(to bottom, var(--orange) 0%, #ffb444 40%, #ffffff 100%);
  }
  .side-nav ul { list-style: none; position: absolute; top: 45px; left: 0; width: 140px; }
  .side-nav li { height: 32px; margin-bottom: 6px; }
  .side-nav a {
    display: block; margin-left: 30px; height: 32px; padding: 6px 10px;
    background: var(--tab); border-radius: 5px 0 0 5px;
    color: var(--ink); text-decoration: none; font-size: 16px; line-height: 20px;
  }
  .side-nav .is-active a {
    margin-left: 8px; height: 34px; margin-top: -1px;
    background: #ffffff; box-shadow: -2px 1px 3px rgba(0,0,0,0.6);
  }

  .content-frame {
    position: absolute; left: 245px; top: 125px; width: 855px; height: 280px;
    border-radius: 8px 8px 0 0;
    background: linear-gradient(to bottom, var(--blue) 0%, #6aa6ff 45%, #ffffff 100%);
  }
  .content-card {
    position: absolute; left: 10px; top: 10px; width: 835px; height: 249px;
    background: linear-gradient(to bottom, #eeeeee, #fafafa);
    border-radius: 5px;
    box-shadow: 0 2px 4px rgba(0,0,0,0.6);
    padding: 19px 20px;
  }
  .content-card h1 {
    font-size: 24px; font-weight: 400; text-transform: uppercase; color: #333; line-height: 1.1;
    margin-bottom: 9px;
  }
  .content-card p {
    font-size: 13.7px; line-height: 23px; color: var(--text);
    margin: 0 0 12px 10px; width: 780px;
  }

  .site-footer {
    position: absolute; left: 0; top: 825px; width: 1200px; height: 75px;
    background: var(--footer); color: var(--footer-text);
  }
  .footer-links { position: absolute; top: 10px; list-style: none; font-size: 13px; line-height: 14px; }
  .footer-links a { color: var(--footer-text); text-decoration: none; }
  .footer-links.primary { left: 100px; }
  .footer-links.secondary { left: 208px; }
  .legal { position: absolute; left: 458px; top: 53px; font-size: 13px; }
  .social { position: absolute; left: 988px; top: 35px; display: flex; gap: 10px; list-style: none; }
  .social li { width: 26px; height: 26px; border-radius: 5px; }
  .social .net-a { background: #3fa9e0; }
  .social .net-b { background: #2f5aa8; }
  .social .net-c { background: #c4302b; }
</style>
</head>
<body>
  <header class="site-header">
    <div class="brand"><span class="brand-mark"></span>wonkibrook</div>
    <ul class="main-nav">
      <li><a href="#">Home</a></li>
      <li><a href="#">Products</a></li>
      <li><a href="#">About</a></li>
      <li><a href="#">Contact</a></li>
    </ul>
    <div class="account-bar">Welcome Milo! <a href="#">Your account</a></div>
    <div class="cart">
      <svg width="56" height="50" viewBox="0 0 56 50" aria-hidden="true">
        <circle cx="4" cy="4" r="2.5" fill="#7a9bb0"/>
        <path d="M5 5 L12 8 L18 36 L50 36" fill="none" stroke="#666" stroke-width="2.5" stroke-linecap="round"/>
        <path d="M13 12 L54 14 L50 32 L17 32 Z" fill="#d8d8d8" stroke="#777" stroke-width="1.5"/>
        <path d="M20 12 L22 32 M28 13 L29 32 M36 13 L36 32 M44 13.5 L43 32 M14 19 L52 21 M15.5 26 L51 27" stroke="#8a8a8a" stroke-width="1"/>
        <circle cx="22" cy="43" r="4.5" fill="#444"/>
        <circle cx="46" cy="43" r="4.5" fill="#444"/>
      </svg>
      <div class="cart-count">[0 items]</div>
    </div>
  </header>

  <nav class="side-nav">
    <ul>
      <li><a href="#">Link</a></li>
      <li class="is-active"><a href="#">Link</a></li>
      <li><a href="#">Link</a></li>
      <li><a href="#">Link</a></li>
    </ul>
  </nav>

  <main class="content-frame">
    <article class="content-card">
      <h1>Current content</h1>
      <p>Content content content content content content content content content content content content content content content content content content content content content content content content content content content content content content</p>
      <p>Content content content content content content content content content content content content content content content content content content content content content content content content content content content content content content</p>
      <p>Content content content content content content content content content content content content content content content content content content content content content content content content content content content content content content</p>
    </article>
  </main>

  <footer class="site-footer">
    <ul class="footer-links primary">
      <li><a href="#">Home</a></li>
      <li><a href="#">Products</a></li>
      <li><a href="#">About</a></li>
      <li><a href="#">Contact</a></li>
    </ul>
    <ul class="footer-links secondary">
      <li><a href="#">News link</a></li>
      <li><a href="#">Article</a></li>
      <li><a href="#">Important</a></li>
      <li><a href="#">Other</a></li>
    </ul>
    <p class="legal">Copyright 2010 and some other legal messages</p>
    <ul class="social">
      <li class="net-a"></li>
      <li class="net-b"></li>
      <li class="net-c"></li>
    </ul>
  </footer>
</body>
</html>
```